Our brand new and excilting business, ZIPPA things, needs a fresh, vibriant and clean website that is

We need a new website designed to sell our ZIPPA things products to schools and fundraisers. We plan to have around 24 items with great images, add to cart and some really new and cool products. This site needs to be clean, fresh and funky, really clean lines, easy to navigate but look really fun and fresh

Target Market(s)

School fundraising. Kids

Industry/Entity Type

Business

Number of Pages Required

4 page

Colors
add136
fbee3d
fbed22
9bcb3c
f78f20

Requirements
Must have
• Fresh, fun and easy to navigate. Great shopping product page that has images of our products and add to cart
Nice to have
• Flashing image availibility
Should not have
• Must not be old and boring

```html
<!DOCTYPE html>
<html lang="en">
<head>
<meta charset="utf-8">
<title>ZIPPA things – The school fundraising specialists</title>
<link rel="stylesheet" href="https://fonts.googleapis.com/css2?family=Open+Sans:wght@400;600;700;800&family=Lato:wght@400;700;900&display=swap">
<style>
:root{
  --green:#9bcb3c;
  --green-dark:#7fb02a;
  --orange:#f78f20;
  --yellow:#fbee3d;
  --yellow-deep:#fbed22;
  --cyan:#add136;
  --ink:#333;
  --muted:#888;
  --dark:#1e1e1e;
  --footer:#2a2a2a;
  --grey-band:#ececec;
  --line:#dedede;
}
*{box-sizing:border-box;margin:0;padding:0}
html,body{width:1200px;height:2528px;overflow:hidden}
body{font-family:"Open Sans",Arial,sans-serif;color:var(--ink);background:#fff;font-size:13px;position:relative}
a{color:inherit;text-decoration:none}

/* header */
.topbar{height:26px;display:flex;justify-content:space-between;align-items:center;padding:0 168px;font-size:12px}
.topbar .promo{color:var(--green-dark);font-weight:700}
.topbar .account{display:flex;gap:16px;color:#666}
.topbar .account span::before{content:"";display:inline-block;width:7px;height:7px;background:var(--orange);border-radius:50%;margin-right:5px}
.masthead{height:118px;display:flex;align-items:center;justify-content:space-between;padding:0 168px;border-bottom:4px solid var(--orange)}
.brand{display:flex;flex-direction:column}
.brand-name{font-family:"Lato",sans-serif;font-weight:900;font-size:50px;color:var(--green);line-height:1;white-space:nowrap}
.brand-tag{font-style:italic;font-size:14px;color:var(--muted);margin-top:4px}
.tools{display:flex;align-items:center;gap:18px}
.search{width:150px;height:28px;border:1px solid var(--line);font-size:11px;color:#aaa;padding:6px 8px}
.phone{font-weight:700;font-size:17px;color:var(--ink);display:flex;align-items:center;gap:6px}
.cart{background:var(--dark);color:#fff;font-size:11px;font-weight:700;padding:6px 12px;line-height:1.2}
.nav{height:32px;background:var(--green);display:flex;align-items:center;padding:0 168px}
.nav a{color:#fff;font-size:10px;font-weight:700;text-transform:uppercase;padding:0 10px;line-height:32px;white-space:nowrap}
.nav a.active{background:var(--orange)}

/* hero */
.hero{position:relative;height:420px;background:radial-gradient(circle at 22% 45%,#6b5a4a 0,#2a2320 30%,#0d0b0f 60%),#0d0b0f;overflow:hidden}
.hero-art{position:absolute;inset:0;background:radial-gradient(ellipse at 62% 38%,rgba(120,255,90,.55),transparent 25%),radial-gradient(ellipse at 75% 30%,rgba(255,60,160,.5),transparent 22%),radial-gradient(ellipse at 85% 45%,rgba(80,140,255,.5),transparent 22%),radial-gradient(ellipse at 55% 25%,rgba(255,200,40,.45),transparent 20%)}
.hero h1{position:absolute;left:680px;top:245px;font-family:"Lato",sans-serif;font-weight:700;color:var(--yellow);font-size:30px;line-height:1.3;text-align:center;white-space:nowrap}
.hero .dots{position:absolute;right:176px;top:382px;display:flex;gap:6px}
.hero .dots i{width:10px;height:10px;border-radius:50%;background:#666}
.hero .dots i:first-child{background:#fff}

/* catalogue + products */
.shop{height:716px;padding:24px 168px 0;display:flex;gap:28px;border-bottom:1px solid var(--line)}
.sidebar{width:232px;flex:none;display:flex;flex-direction:column;gap:20px}
.promo-box{border:1px solid var(--line);height:250px;padding:18px 14px;text-align:center}
.promo-box .year{font-weight:800;font-size:20px;color:var(--ink)}
.promo-box .new{color:var(--orange);font-weight:800;font-size:17px;margin-top:8px}
.promo-box .cat{font-weight:800;font-size:15px}
.promo-box .site{font-size:11px;color:var(--muted);margin-top:4px}
.cat-row{display:flex;justify-content:space-between;align-items:center;margin-top:18px}
.cat-cover{width:86px;height:96px;background:linear-gradient(135deg,var(--green),var(--yellow))}
.download{background:var(--orange);color:#fff;font-weight:800;font-size:12px;padding:8px 12px;border-radius:3px}
.refund{height:182px;background:var(--yellow);display:flex;flex-direction:column;align-items:center;justify-content:center;gap:10px}
.seal{width:84px;height:84px;border-radius:50%;background:#e9b81e;border:4px solid #fff}
.refund p{font-weight:800;font-size:17px;text-align:center;line-height:1.15;color:var(--dark)}
.charity{height:176px;background:var(--green);display:flex;flex-direction:column;align-items:center;justify-content:center;gap:10px;color:#fff}
.charity .icon{width:70px;height:56px;background:rgba(255,255,255,.35);border-radius:6px}
.charity p{font-weight:800;font-size:16px;text-align:center;line-height:1.2;color:var(--dark)}
.popular{flex:1}
.popular-head{height:30px;background:var(--orange);color:#fff;font-weight:800;font-size:16px;line-height:30px;padding-left:12px;position:relative}
.popular-head::after{content:"";position:absolute;right:0;top:0;border-left:16px solid transparent;border-top:30px solid #fff}
.grid{display:grid;grid-template-columns:repeat(4,1fr);gap:0 12px;padding-top:12px}
.card{height:318px;padding:14px 8px;display:flex;flex-direction:column;align-items:center;position:relative}
.thumb{width:128px;height:128px;border-radius:50%}
.t1{background:radial-gradient(circle at 40% 40%,#ff9ad1,#3a2670 70%)}
.t2{background:radial-gradient(circle at 50% 40%,#7ef0ff,#0b2c6a 70%)}
.t3{background:radial-gradient(circle at 50% 50%,#ffe04a,#7b2fa8 70%)}
.badge{position:absolute;top:14px;right:18px;width:36px;height:18px;background:var(--green);color:#fff;font-size:9px;font-weight:800;text-align:center;line-height:18px}
.badge.sale{background:var(--orange)}
.price{font-weight:800;font-size:19px;color:#555;margin-top:14px}
.desc{font-size:10px;color:var(--muted);text-align:center;line-height:1.45;margin-top:6px;width:130px;height:30px;overflow:hidden}
.actions{display:flex;gap:4px;margin-top:12px}
.add{background:var(--dark);color:#fff;font-size:10px;font-weight:700;padding:5px 10px;white-space:nowrap}
.fav{width:24px;height:24px;background:var(--orange);display:flex;align-items:center;justify-content:center}

/* review */
.review{height:360px;background:var(--grey-band);text-align:center;padding-top:34px}
.review h2{font-weight:800;font-size:24px;color:#444}
.review h2::after{content:"";display:block;width:48px;height:3px;background:var(--orange);margin:10px auto 0}
.review .intro{font-size:11px;color:var(--muted);margin-top:10px}
.quote{width:840px;height:128px;margin:24px auto 0;background:#fff;border:1px solid var(--line);display:flex;align-items:center;gap:22px;padding:0 26px;text-align:left}
.quote p{flex:1;font-size:11.5px;color:#777;font-style:italic;line-height:1.6}
.avatar{width:84px;height:84px;flex:none;border-radius:50%;background:linear-gradient(135deg,#c9a88b,#6b5344);border:4px solid var(--grey-band)}
.reviewer{margin-top:16px;font-size:11px;font-weight:700;color:#666}

/* newsletter */
.news{height:320px;background:#151515;position:relative;overflow:hidden}
.news-art{position:absolute;right:150px;top:0;width:420px;height:320px;background:radial-gradient(circle at 40% 40%,rgba(255,90,200,.6),transparent 45%),radial-gradient(circle at 70% 60%,rgba(120,80,255,.5),transparent 40%),#151515}
.news-copy{position:absolute;left:240px;top:100px;width:430px;text-align:center;color:#fff}
.news-copy h3{font-size:15px;font-weight:700;line-height:1.45}
.news-copy p{font-size:10px;color:#aaa;margin-top:16px;line-height:1.5}
.signup{position:absolute;left:270px;top:226px;display:flex}
.signup .field{width:250px;height:32px;background:#fff;font-size:11px;color:#aaa;padding:8px 10px}
.signup .submit{height:32px;background:var(--yellow);color:var(--dark);font-weight:800;font-size:12px;padding:8px 16px}

/* service strip */
.services{height:172px;display:flex;justify-content:center;gap:34px;align-items:center}
.service{width:176px;height:58px;border:1px solid var(--line);display:flex;align-items:center;gap:10px;padding:0 10px}
.service .ico{width:40px;height:40px;flex:none;border-radius:50%;display:flex;align-items:center;justify-content:center}
.service .ico.orange{background:var(--orange)}
.service .ico.green{background:var(--green)}
.service strong{display:block;font-size:13px;color:var(--ink)}
.service small{font-size:10px;color:var(--muted)}

/* footer */
.footer{height:316px;background:var(--footer);display:flex;gap:36px;padding:22px 168px 0;color:#bbb}
.footer-brand{width:210px;flex:none;background:#222;padding:16px;height:270px}
.footer-brand .brand-name{font-size:28px}
.footer-brand p{font-size:10px;line-height:1.6;margin-top:10px;color:#999}
.footer-brand .more{display:inline-block;margin-top:12px;background:var(--orange);color:#fff;font-size:10px;font-weight:700;padding:5px 10px}
.footer-col{width:170px}
.footer-col h4{color:#fff;font-size:13px;font-weight:700;margin-bottom:10px;white-space:nowrap}
.footer-col li{list-style:none;font-size:10.5px;line-height:1.75;white-space:nowrap}
.footer-col h4.sub{margin-top:14px}
.bottom{height:48px;background:#111;display:flex;align-items:center;justify-content:space-between;padding:0 168px;font-size:10px;color:#888}
.social{display:flex;gap:6px}
.social i{width:22px;height:22px;border-radius:50%;background:#444}
</style>
</head>
<body>

<header>
  <div class="topbar">
    <span class="promo">10 Free Prizes When You Spend Over £30!</span>
    <div class="account"><span>LOGIN</span><span>MY ACCOUNT</span><span>CHECKOUT</span></div>
  </div>
  <div class="masthead">
    <div class="brand">
      <span class="brand-name">ZIPPA things</span>
      <span class="brand-tag">The school fundraising specialists</span>
    </div>
    <div class="tools">
      <div class="search">Enter Search Here</div>
      <div class="phone">
        <svg width="16" height="16" viewBox="0 0 24 24"><path fill="#f78f20" d="M6.6 10.8a15 15 0 006.6 6.6l2.2-2.2c.3-.3.7-.4 1-.2 1.1.4 2.3.6 3.6.6.6 0 1 .4 1 1V20c0 .6-.4 1-1 1A17 17 0 013 4c0-.6.4-1 1-1h3.5c.6 0 1 .4 1 1 0 1.3.2 2.5.6 3.6.1.3 0 .7-.2 1z"/></svg>
        123 456 7890
      </div>
      <div class="cart">CART<br>0 items</div>
    </div>
  </div>
  <nav class="nav">
    <a class="active">Home</a><a>Glow Sticks</a><a>Glow &amp; Light Up Novelties</a><a>Glowing Necklaces</a><a>Glow Bracelets</a><a>Party Supplies</a><a>Wholesale</a><a>Contact</a>
  </nav>
</header>

<section class="hero">
  <div class="hero-art" role="img" aria-label="Photo of a smiling girl holding colourful glowing necklaces and bracelets in the dark"></div>
  <h1>Buy Glow Necklaces, Glow Bracelets<br>Glowsticks &amp; MUCH More!</h1>
  <div class="dots"><i></i><i></i><i></i></div>
</section>

<section class="shop">
  <aside class="sidebar">
    <div class="promo-box">
      <div class="year">2015/2016</div>
      <div class="new">NEW</div>
      <div class="cat">CATALOGUE</div>
      <div class="site">zippathings.example</div>
      <div class="cat-row">
        <div class="cat-cover" role="img" aria-label="Catalogue cover with glowing products"></div>
        <span class="download">DOWNLOAD</span>
      </div>
    </div>
    <div class="refund">
      <div class="seal"></div>
      <p>REPLACE OR<br>REFUND OFFERED</p>
    </div>
    <div class="charity">
      <div class="icon"></div>
      <p>PTA AND CHARITY<br>DISCOUNTS</p>
    </div>
  </aside>

  <div class="popular">
    <div class="popular-head">Most Popular</div>
    <div class="grid">
      <div class="card"><div class="thumb t1" role="img" aria-label="Glow sticks product photo"></div><span class="badge">NEW</span><div class="price">$65.95</div><div class="desc">Bright glow sticks in mixed colours, pack of 50</div><div class="actions"><span class="add">Add To Cart</span><span class="fav"><svg width="12" height="12" viewBox="0 0 24 24"><path fill="#fff" d="M12 21l-1.4-1.3C5.4 15 2 12 2 8.5 2 5.4 4.4 3 7.5 3c1.7 0 3.4.8 4.5 2.1C13.1 3.8 14.8 3 16.5 3 19.6 3 22 5.4 22 8.5c0 3.5-3.4 6.5-8.6 11.2z"/></svg></span></div></div>
      <div class="card"><div class="thumb t2" role="img" aria-label="Glow bracelets product photo"></div><div class="price">$86.00</div><div class="desc">Glow bracelets with connectors, tube of 100</div><div class="actions"><span class="add">Add To Cart</span><span class="fav"><svg width="12" height="12" viewBox="0 0 24 24"><path fill="#fff" d="M12 21l-1.4-1.3C5.4 15 2 12 2 8.5 2 5.4 4.4 3 7.5 3c1.7 0 3.4.8 4.5 2.1C13.1 3.8 14.8 3 16.5 3 19.6 3 22 5.4 22 8.5c0 3.5-3.4 6.5-8.6 11.2z"/></svg></span></div></div>
      <div class="card"><div class="thumb t3" role="img" aria-label="Party supplies product photo"></div><div class="price">$45.20</div><div class="desc">Party supplies bundle with glasses and wands</div><div class="actions"><span class="add">Add To Cart</span><span class="fav"><svg width="12" height="12" viewBox="0 0 24 24"><path fill="#fff" d="M12 21l-1.4-1.3C5.4 15 2 12 2 8.5 2 5.4 4.4 3 7.5 3c1.7 0 3.4.8 4.5 2.1C13.1 3.8 14.8 3 16.5 3 19.6 3 22 5.4 22 8.5c0 3.5-3.4 6.5-8.6 11.2z"/></svg></span></div></div>
      <div class="card"><div class="thumb t1" role="img" aria-label="Glow necklaces product photo"></div><div class="price">$45.20</div><div class="desc">Glow necklaces in six colours, pack of 50</div><div class="actions"><span class="add">Add To Cart</span><span class="fav"><svg width="12" height="12" viewBox="0 0 24 24"><path fill="#fff" d="M12 21l-1.4-1.3C5.4 15 2 12 2 8.5 2 5.4 4.4 3 7.5 3c1.7 0 3.4.8 4.5 2.1C13.1 3.8 14.8 3 16.5 3 19.6 3 22 5.4 22 8.5c0 3.5-3.4 6.5-8.6 11.2z"/></svg></span></div></div>
      <div class="card"><div class="thumb t1" role="img" aria-label="Glow sticks product photo"></div><span class="badge sale">SALE</span><div class="price">$65.95</div><div class="desc">Bright glow sticks in mixed colours, pack of 50</div><div class="actions"><span class="add">Add To Cart</span><span class="fav"><svg width="12" height="12" viewBox="0 0 24 24"><path fill="#fff" d="M12 21l-1.4-1.3C5.4 15 2 12 2 8.5 2 5.4 4.4 3 7.5 3c1.7 0 3.4.8 4.5 2.1C13.1 3.8 14.8 3 16.5 3 19.6 3 22 5.4 22 8.5c0 3.5-3.4 6.5-8.6 11.2z"/></svg></span></div></div>
      <div class="card"><div class="thumb t2" role="img" aria-label="Glow bracelets product photo"></div><div class="price">$86.00</div><div class="desc">Glow bracelets with connectors, tube of 100</div><div class="actions"><span class="add">Add To Cart</span><span class="fav"><svg width="12" height="12" viewBox="0 0 24 24"><path fill="#fff" d="M12 21l-1.4-1.3C5.4 15 2 12 2 8.5 2 5.4 4.4 3 7.5 3c1.7 0 3.4.8 4.5 2.1C13.1 3.8 14.8 3 16.5 3 19.6 3 22 5.4 22 8.5c0 3.5-3.4 6.5-8.6 11.2z"/></svg></span></div></div>
      <div class="card"><div class="thumb t3" role="img" aria-label="Party supplies product photo"></div><div class="price">$45.20</div><div class="desc">Party supplies bundle with glasses and wands</div><div class="actions"><span class="add">Add To Cart</span><span class="fav"><svg width="12" height="12" viewBox="0 0 24 24"><path fill="#fff" d="M12 21l-1.4-1.3C5.4 15 2 12 2 8.5 2 5.4 4.4 3 7.5 3c1.7 0 3.4.8 4.5 2.1C13.1 3.8 14.8 3 16.5 3 19.6 3 22 5.4 22 8.5c0 3.5-3.4 6.5-8.6 11.2z"/></svg></span></div></div>
      <div class="card"><div class="thumb t2" role="img" aria-label="Light up novelties product photo"></div><div class="price">$45.20</div><div class="desc">Light up novelty wands with flashing star tips</div><div class="actions"><span class="add">Add To Cart</span><span class="fav"><svg width="12" height="12" viewBox="0 0 24 24"><path fill="#fff" d="M12 21l-1.4-1.3C5.4 15 2 12 2 8.5 2 5.4 4.4 3 7.5 3c1.7 0 3.4.8 4.5 2.1C13.1 3.8 14.8 3 16.5 3 19.6 3 22 5.4 22 8.5c0 3.5-3.4 6.5-8.6 11.2z"/></svg></span></div></div>
    </div>
  </div>
</section>

<section class="review">
  <h2>Our Customer Review</h2>
  <p class="intro">Hear what schools and parent groups say about their fundraising nights with us.</p>
  <div class="quote">
    <svg width="30" height="26" viewBox="0 0 30 26"><path fill="#9bcb3c" d="M0 26V14C0 6 4 1 12 0v5c-4 1-6 4-6 9h6v12zm18 0V14c0-8 4-13 12-14v5c-4 1-6 4-6 9h6v12z"/></svg>
    <p>Our school disco was a huge hit this year. The glow bracelets and necklaces arrived quickly, the children loved them and we raised far more than we expected for new playground equipment. Ordering was simple and the team were friendly and helpful from start to finish.</p>
    <div class="avatar" role="img" aria-label="Portrait photo of the reviewer"></div>
  </div>
  <p class="reviewer">Sam Porter, Leeds, UK</p>
</section>

<section class="news">
  <div class="news-art" role="img" aria-label="Photo of a girl holding a glowing light up star wand"></div>
  <div class="news-copy">
    <h3>Keep Up To Date With The Latest From Brightside.<br>We Love Pets.</h3>
    <p>Join our mailing list to hear about new products, offers and<br>fundraising tips for your next school event.</p>
  </div>
  <div class="signup"><div class="field">Enter your email address</div><div class="submit">SUBMIT</div></div>
</section>

<section class="services">
  <div class="service"><span class="ico orange"><svg width="22" height="16" viewBox="0 0 22 16"><path fill="#fff" d="M0 1h13v10H0zM14 4h4l4 4v3h-8z"/><circle cx="5" cy="13" r="2.5" fill="#fff"/><circle cx="17" cy="13" r="2.5" fill="#fff"/></svg></span><div><strong>Delivery</strong><small>Information</small></div></div>
  <div class="service"><span class="ico green"><svg width="20" height="20" viewBox="0 0 24 24"><path fill="none" stroke="#fff" stroke-width="2.5" d="M4 12a8 8 0 108-8H7M9 1L6 4l3 3"/></svg></span><div><strong>Returns</strong><small>Policy</small></div></div>
  <div class="service"><span class="ico orange"><svg width="14" height="20" viewBox="0 0 14 20"><path fill="none" stroke="#fff" stroke-width="2.5" d="M2 5a5 5 0 1110 0c0 3-5 4-5 8"/><circle cx="7" cy="18" r="1.6" fill="#fff"/></svg></span><div><strong>Questions?</strong><small>Contact Us</small></div></div>
  <div class="service"><span class="ico orange"><svg width="18" height="18" viewBox="0 0 24 24"><path fill="#fff" d="M6.6 10.8a15 15 0 006.6 6.6l2.2-2.2c.3-.3.7-.4 1-.2 1.1.4 2.3.6 3.6.6.6 0 1 .4 1 1V20c0 .6-.4 1-1 1A17 17 0 013 4c0-.6.4-1 1-1h3.5c.6 0 1 .4 1 1 0 1.3.2 2.5.6 3.6.1.3 0 .7-.2 1z"/></svg></span><div><strong>Let Us Help</strong><small>Contact Us</small></div></div>
</section>

<footer>
  <div class="footer">
    <div class="footer-brand">
      <span class="brand-name">ZIPPA things</span>
      <p>We help schools, clubs and charities raise more with bright, fun glow products delivered fast at great prices all year round.</p>
      <span class="more">READ MORE</span>
    </div>
    <div class="footer-col">
      <h4>Quick Link</h4>
      <ul><li>Home</li><li>About Us</li><li>Glow Sticks</li><li>Glow &amp; Light Up Novelties</li><li>Glowing Necklaces</li><li>Glow Bracelets</li><li>Party Supplies</li><li>Wholesale</li><li>Contact Us</li></ul>
    </div>
    <div class="footer-col">
      <h4>Help and Information</h4>
      <ul><li>Contact Us</li><li>Customer Service Info</li><li>Our Customer Guarantee</li><li>Delivery Information</li><li>Quality and Safety Information</li></ul>
      <h4 class="sub">Wholesale Products</h4>
      <ul><li>Wholesale Glow Sticks</li><li>Wholesale Flashing Novelties</li></ul>
    </div>
    <div class="footer-col">
      <h4>Other Information</h4>
      <ul><li>Ordering and Payment Options</li><li>Privacy Policy</li><li>Terms and Conditions</li><li>Returns Information</li><li>Cookie Policy</li></ul>
      <ul style="margin-top:14px"><li>Printed Glow Sticks</li><li>Fundraising Ideas</li></ul>
    </div>
  </div>
  <div class="bottom">
    <span>© 2015 ZIPPA things. All rights reserved.</span>
    <div class="social"><i></i><i></i><i></i><i></i></div>
  </div>
</footer>

</body>
</html>
```